MERIDIAN MAILWORKS - DIRECT MAIL BUSINESS CARD

Meridian Mailworks, 718 E Larkin Ave, WESTBROOK OK 73510 405-555-0187 email - dalew482@quillpost.example Owner Dale Whitford Serving customers since 1989, Product - Direct mail marketing

Target Market(s)

Businesses,churches and non-profits

Industry/Entity Type

Marketing

Contact Information for Business Card

Dark blue UV coated card with white letters on front. Maybe add a sketch of a mail addressing machine. On the back either Dark blue or full color with the sketch of a postman throwing a letter towards a world globe, with the phrase reach your world. Or the postman throwing a letter towards a archery target with the phrase, reach your target market.

Font styles to use
Serif

Colors
0355a3

Requirements
Must have
• MERIDIAN MAILWORKS
• 718 E LARKIN AVE
• WESTBROOK OK 73510
• 405-555-0187
• dalew482@quillpost.example
• DALE WHITFORD, OWNER
• DIRECT MAIL MARKETING
Nice to have
• SERVING CUSTOMERS SINCE 1989 SKETCH OF MAIL ADDRESSING EQUIPMENT, IN THE BACKGROUND, ON THE FRONT
• ON THE BACK, SKETCH OF POSTMAN THROWING LETTER TO THE WORLD
• GLOBE, WITH THE PHRASE, REACH YOUR WORLD, OR THE LETTER TO A TARGET, WITH PHRASE, REACH YOUR TARGET MARKET
Should not have
• PHOTOS OR FLOWERS

```html
<!DOCTYPE html>
<html lang="en">
<head>
<meta charset="utf-8">
<title>Meridian Mailworks – Business Card</title>
<link rel="stylesheet" href="https://fonts.googleapis.com/css2?family=Montserrat:wght@700&family=Open+Sans:wght@400;600;700&display=swap">
<style>
  :root {
    --navy: #2b3990;
    --brand-blue: #1f6fae;
    --ink-blue: #2a5ea8;
    --white: #ffffff;
    --stage: #d9dbe0;
    --globe-tint: rgba(255,255,255,0.12);
  }
  * { margin: 0; padding: 0; box-sizing: border-box; }
  html, body { width: 1200px; height: 900px; overflow: hidden; background: var(--stage); }
  .canvas { position: relative; width: 1200px; height: 900px; }

  .card {
    position: absolute;
    width: 680px; height: 390px;
    border-radius: 26px;
    overflow: hidden;
    box-shadow: 0 10px 28px rgba(0,0,0,0.18);
  }

  /* Front */
  .card-front { left: 110px; top: 60px; background: var(--white); }
  .front-brand {
    position: absolute; left: 0; right: 0; top: 70px;
    display: flex; flex-direction: column; align-items: center;
  }
  .brand-mark { width: 110px; height: 110px; border-radius: 50%; background: var(--navy); }
  .brand-name {
    margin-top: 26px;
    font-family: "Montserrat", sans-serif; font-weight: 700;
    font-size: 19px; letter-spacing: 0.5px; color: var(--ink-blue);
    white-space: nowrap;
  }
  .front-base { position: absolute; left: 0; right: 0; bottom: 0; height: 30px; background: var(--brand-blue); }
  .front-tagline {
    position: absolute; right: 0; bottom: 18px; width: 400px; height: 48px;
    background: var(--navy);
    display: flex; align-items: center; justify-content: center;
    font-family: "Open Sans", sans-serif; font-size: 17px; letter-spacing: 1.5px; color: var(--white);
  }

  /* Back */
  .card-back { left: 410px; top: 470px; background: var(--navy); }
  .back-top-strip { position: absolute; right: 0; top: 0; width: 200px; height: 14px; background: var(--brand-blue); }
  .globe-backdrop { position: absolute; left: 200px; top: 20px; width: 330px; height: 330px; }
  .back-brand {
    position: absolute; left: 40px; top: 145px; width: 250px;
    display: flex; flex-direction: column; align-items: center;
  }
  .back-brand .brand-mark { width: 76px; height: 76px; background: var(--white); }
  .back-brand .brand-name { margin-top: 18px; font-size: 13px; color: var(--white); letter-spacing: 0.3px; }
  .divider { position: absolute; left: 310px; top: 70px; width: 2px; height: 150px; background: rgba(255,255,255,0.8); }
  .contact { position: absolute; left: 336px; top: 72px; color: var(--white); font-family: "Open Sans", sans-serif; }
  .contact-name { font-family: "Montserrat", sans-serif; font-weight: 700; font-size: 26px; letter-spacing: 0.5px; }
  .contact-role { font-size: 15px; margin-bottom: 8px; }
  .contact-line { font-size: 16px; line-height: 1.35; display: flex; align-items: center; gap: 8px; white-space: nowrap; }
  .contact-line svg { width: 13px; height: 13px; flex: none; }
  .back-base { position: absolute; left: 0; right: 0; bottom: 0; height: 24px; background: var(--brand-blue); }
  .back-tagline {
    position: absolute; right: 0; bottom: 10px; width: 380px; height: 38px;
    background: var(--white);
    display: flex; align-items: center; justify-content: center;
    font-family: "Open Sans", sans-serif; font-size: 17px; letter-spacing: 1px; color: var(--navy);
  }
</style>
</head>
<body>
<main class="canvas">

  <section class="card card-front">
    <div class="front-brand">
      <div class="brand-mark"></div>
      <div class="brand-name">MERIDIAN MAILWORKS</div>
    </div>
    <div class="front-base"></div>
    <div class="front-tagline">DIRECT MAIL MARKETING</div>
  </section>

  <section class="card card-back">
    <div class="back-top-strip"></div>
    <svg class="globe-backdrop" viewBox="0 0 330 330" role="img" aria-label="Faint world globe backdrop">
      <circle cx="165" cy="165" r="165" fill="var(--globe-tint)"/>
    </svg>
    <div class="back-brand">
      <div class="brand-mark"></div>
      <div class="brand-name">MERIDIAN MAILWORKS</div>
    </div>
    <div class="divider"></div>
    <div class="contact">
      <div class="contact-name">DALE WHITFORD</div>
      <div class="contact-role">OWNER</div>
      <div class="contact-line">718 E LARKIN AVE</div>
      <div class="contact-line">WESTBROOK OK 73510</div>
      <div class="contact-line">
        <svg viewBox="0 0 24 24" aria-hidden="true"><path fill="#fff" d="M6.6 10.8a15 15 0 0 0 6.6 6.6l2.2-2.2c.3-.3.7-.4 1-.2 1.1.4 2.3.6 3.6.6.6 0 1 .4 1 1V20c0 .6-.4 1-1 1A17 17 0 0 1 3 4c0-.6.4-1 1-1h3.5c.6 0 1 .4 1 1 0 1.3.2 2.5.6 3.6.1.3 0 .7-.2 1z"/></svg>
        405-555-0187
      </div>
      <div class="contact-line">
        <svg viewBox="0 0 24 24" aria-hidden="true"><rect x="2" y="5" width="20" height="14" rx="1.5" fill="none" stroke="#fff" stroke-width="2"/><path d="M2.5 6l9.5 7 9.5-7" fill="none" stroke="#fff" stroke-width="2"/></svg>
        dalew482@quillpost.example
      </div>
    </div>
    <div class="back-base"></div>
    <div class="back-tagline">SERVING CUSTOMERS SINCE 1989</div>
  </section>

</main>
</body>
</html>
```